6.5x9" Postcard Project for Organic and Sustainably powered Lawn Care Service

Hello,

Looking for a 6.6"Hx9"W postcard for my first direct mail project.

We are a full service lawn care company providing organic lawn treatment programs and full service lawn maintenance with solar powered electric equipment (and sometimes propane/biodiesel equipment for larger lawns and spaces). We are brand new to Houston and are in the midst of our rollout. This will be our first structured marketing effort so we want something that will grab people's attention as well as really do a good job telling people what we're about!

I have some logos and designs from some other products from the other franchisees and was wanting something similar.

Some of our info and "catch phrases":

Site: www.BrightFernYardWorksTexan.com

Phone Number: 713.580.2143

"The Neighborhood's Healthiest Lawn"

"Changing The Way America Mows The Lawn"

"Come Clean"

"Clean. Green. Organic."
If at all possible please include standard every day direct mail indicia as well.

Please let me know if there is anything else I can do to assist making the best product possible.

Thanks!

Marcus

Target Market(s)

Organic and Environmentally Minded people needing lawn service.

Industry/Entity Type

Lawn Care

Requirements
Must have
• Logo, website, phone number, invitation for free estimate

```html
<!DOCTYPE html>
<html lang="en">
<head>
<meta charset="utf-8">
<title>Bright Fern Yard Works – Direct Mail Postcard</title>
<link href="https://fonts.googleapis.com/css2?family=Archivo+Black&family=Arimo:wght@400;700&family=Cinzel:wght@400;700&family=Alfa+Slab+One&family=Roboto+Slab:wght@400;700&display=swap" rel="stylesheet">
<style>
  :root{
    --stage:#231f1e;
    --white:#ffffff;
    --sky-top:#9cc7ec;
    --sky-mid:#cfe4f5;
    --grass-dark:#3f8a1f;
    --grass:#6cb33a;
    --leaf:#7bc043;
    --gold:#ebb923;
    --brown:#6b3f1c;
    --tan:#d19a66;
    --soft-blue:#8cb5dd;
    --olive:#6f9a3d;
    --sky-logo:#6ec6ee;
    --ink:#1e1e1e;
    --body-ink:#2e3a45;
  }
  *{box-sizing:border-box;margin:0;padding:0}
  html,body{width:1200px;height:1200px;overflow:hidden;background:var(--stage)}
  .stage{position:relative;width:1200px;height:1200px;background:var(--stage)}
  .card{position:absolute;width:768px;height:556px;background:var(--white);overflow:hidden}
  .card--front{left:214px;top:34px}
  .card--back{left:215px;top:618px;height:555px}
  .abs{position:absolute}

  /* front */
  .front-scene{left:0;top:0;width:768px;height:470px;
    background:linear-gradient(180deg,var(--sky-top) 0%,var(--sky-mid) 42%,#e8f1f7 55%,var(--grass) 70%,var(--grass-dark) 100%)}
  .front-wave{left:0;top:360px;width:768px;height:196px}
  .come-clean{left:380px;top:64px;font-family:"Archivo Black",sans-serif;font-size:30px;color:var(--leaf);letter-spacing:.3px;line-height:1.1;white-space:nowrap}
  .mascot-small{left:634px;top:44px;width:56px;height:56px;border-radius:26px;background:linear-gradient(180deg,#8a5a30,var(--leaf))}
  .child-photo{left:510px;top:110px;width:220px;height:256px;border-radius:18px;
    background:linear-gradient(180deg,#e9dccc 0%,#f0d46a 45%,#e8c23a 70%,#5f9f32 100%)}
  .headline{left:62px;top:112px;font-family:"Cinzel",serif;font-weight:400;line-height:1.12;color:var(--olive)}
  .headline .free{font-size:56px;color:var(--gold)}
  .headline .lead{font-size:35px;color:var(--soft-blue)}
  .headline .olive{color:var(--olive)}
  .headline .line{display:block;font-size:38px}
  .cta-bubble{left:63px;top:346px;width:354px;height:108px}
  .cta-text{left:63px;top:366px;width:354px;text-align:center;font-family:"Roboto Slab",serif;color:var(--white);font-size:23px;line-height:1.1}
  .cta-text strong{font-weight:700}
  .front-url{left:62px;top:472px;width:356px;text-align:center;font-family:"Cinzel",serif;font-weight:700;font-size:15.5px;color:var(--brown);letter-spacing:.3px}
  .front-phone{left:62px;top:490px;width:356px;text-align:center;font-family:"Cinzel",serif;font-size:25px;color:var(--sky-logo);display:flex;justify-content:center;align-items:center;gap:6px}
  .front-brand{left:442px;top:400px;width:264px;display:flex;align-items:center;justify-content:center;gap:10px}
  .brand-dot{width:26px;height:26px;border-radius:50%;background:var(--leaf);flex:none}
  .brand-name{font-family:"Roboto Slab",serif;font-weight:700;color:var(--grass);line-height:1.05}
  .front-brand .brand-name{font-size:27px}

  /* back */
  .back-panel{left:0;top:0;width:454px;height:555px;
    background:linear-gradient(180deg,#78c6ef 0%,#a9dcf5 45%,#d7eef8 62%,var(--grass) 80%,var(--grass-dark) 100%)}
  .mascot-large{left:57px;top:50px;width:168px;height:144px;border-radius:60px;background:linear-gradient(180deg,#8a5a30 0%,var(--leaf) 60%,var(--gold) 100%)}
  .slogan{left:233px;top:60px;font-family:"Alfa Slab One",serif;font-weight:400;font-size:37px;line-height:1.15;letter-spacing:.5px;white-space:nowrap}
  .slogan .s1{color:var(--tan);display:block}
  .slogan .s2{color:var(--leaf);display:block}
  .slogan .s3{color:var(--brown);display:block;font-size:31px}
  .is-title{left:54px;top:202px;font-family:"Archivo Black",sans-serif;font-size:16px;color:var(--gold)}
  .benefits{left:54px;top:230px;width:390px;list-style:none;font-family:"Arimo",sans-serif;font-size:13px;line-height:16px;color:var(--body-ink)}
  .benefits li{position:relative;padding-left:19px;margin-bottom:14px}
  .benefits svg{position:absolute;left:0;top:3px}
  .info-bubble{left:103px;top:379px;width:232px;height:82px}
  .info-text{left:103px;top:398px;width:232px;text-align:center;font-family:"Arimo",sans-serif;font-weight:700;font-size:16px;line-height:17px;color:var(--white)}
  .back-url{left:0;top:465px;width:454px;text-align:center;font-family:"Cinzel",serif;font-weight:700;font-size:15px;color:var(--white);letter-spacing:.3px}
  .back-phone{left:0;top:484px;width:454px;text-align:center;font-family:"Cinzel",serif;font-size:25px;color:var(--white);display:flex;justify-content:center;align-items:center;gap:5px}
  .indicia{left:649px;top:48px;width:72px;height:61px;border:1px solid var(--ink);font-family:"Arimo",sans-serif;font-size:8.5px;line-height:11.4px;text-align:center;color:var(--ink);padding-top:3px}
  .ecrwss{left:493px;top:144px;font-family:"Roboto Slab",serif;font-weight:700;font-size:10.5px;color:var(--ink)}
  .postal{left:495px;top:163px;font-family:"Arimo",sans-serif;font-size:9.5px;line-height:11px;color:var(--ink)}
  .back-brand{left:500px;top:250px;width:200px;display:flex;align-items:center;justify-content:center;gap:8px}
  .back-brand .brand-name{font-size:19px}
  .back-brand .brand-dot{width:20px;height:20px}
  .tagline{left:480px;top:318px;width:240px;text-align:center;font-family:"Cinzel",serif;font-weight:700;font-size:15px;line-height:16px;color:var(--brown)}
</style>
</head>
<body>
<main class="stage">

  <section class="card card--front" aria-label="Postcard front">
    <div class="abs front-scene" role="img" aria-label="Photo of bright blue sky and tall green lawn grass beside a house"></div>
    <svg class="abs front-wave" viewBox="0 0 768 196" aria-hidden="true">
      <path d="M0 34 C60 0 140 12 200 28 C260 12 340 6 400 36 C470 20 560 0 620 18 C690 0 740 8 768 22 L768 196 L0 196 Z" fill="#ffffff"/>
    </svg>
    <div class="abs come-clean">COME CLEAN</div>
    <div class="abs mascot-small" role="img" aria-label="Small mascot illustration beside the slogan"></div>
    <div class="abs child-photo" role="img" aria-label="Photo of a toddler in a yellow outfit and safety goggles sitting in the grass"></div>

    <h1 class="abs headline">
      <span class="free">FREE</span> <span class="lead">YOUR</span> <span class="lead olive">LAWN</span>
      <span class="line"><span style="color:var(--soft-blue)">FROM</span> DANGEROUS</span>
      <span class="line">CHEMICALS</span>
    </h1>

    <svg class="abs cta-bubble" viewBox="0 0 354 108" aria-hidden="true">
      <path d="M28 12 H166 L177 0 L188 12 H326 Q354 12 354 40 V80 Q354 108 326 108 H28 Q0 108 0 80 V40 Q0 12 28 12 Z" fill="#ebb923"/>
    </svg>
    <p class="abs cta-text">Contact us to learn<br>more and schedule your<br><strong>FREE</strong> ESTIMATE</p>

    <div class="abs front-url">WWW.BRIGHTFERNYARDWORKSTEXAN.COM</div>
    <div class="abs front-phone">
      <svg width="22" height="22" viewBox="0 0 24 24" aria-hidden="true"><circle cx="12" cy="12" r="10.5" fill="none" stroke="#6ec6ee" stroke-width="1.5"/><path d="M9 6.5 L11 9.5 L9.8 11 Q11 13.6 13 14.4 L14.5 13.2 L17.5 15.2 L16.2 17.5 Q10 17 7 9 Z" fill="#6ec6ee"/></svg>
      <span>(713) 580-2143</span>
    </div>

    <div class="abs front-brand">
      <span class="brand-dot"></span>
      <span class="brand-name">Bright Fern<br>Yard Works</span>
    </div>
  </section>

  <section class="card card--back" aria-label="Postcard back">
    <div class="abs back-panel" role="img" aria-label="Soft blue sky fading into a close-up of green grass"></div>
    <div class="abs mascot-large" role="img" aria-label="Mascot illustration with crossed arms and a leaf cape"></div>
    <h2 class="abs slogan"><span class="s1">CLEAN.</span><span class="s2">GREEN.</span><span class="s3">ORGANIC.</span></h2>

    <div class="abs is-title">BRIGHT FERN YARD WORKS IS:</div>
    <ul class="abs benefits">
      <li><svg width="12" height="10" viewBox="0 0 12 10" aria-hidden="true"><path d="M1 5 L4.5 8.5 L11 1" fill="none" stroke="#6cb33a" stroke-width="2"/></svg>Organic treatment programs to ensure your lawn is healthy, beautiful and safe for children, pets, and our local environment.</li>
      <li><svg width="12" height="10" viewBox="0 0 12 10" aria-hidden="true"><path d="M1 5 L4.5 8.5 L11 1" fill="none" stroke="#6cb33a" stroke-width="2"/></svg>Clean and quiet electric equipment powered by mobile solar charging units.</li>
      <li><svg width="12" height="10" viewBox="0 0 12 10" aria-hidden="true"><path d="M1 5 L4.5 8.5 L11 1" fill="none" stroke="#6cb33a" stroke-width="2"/></svg>Lawn care practices that maximize water conservation and nutrient uptake while minimizing weed growth.</li>
    </ul>

    <svg class="abs info-bubble" viewBox="0 0 232 82" aria-hidden="true">
      <path d="M24 8 H108 L116 0 L124 8 H208 Q232 8 232 32 V52 Q232 74 208 74 H124 L116 82 L108 74 H24 Q0 74 0 52 V32 Q0 8 24 8 Z" fill="#ebb923"/>
    </svg>
    <p class="abs info-text">For More Information<br>Please Visit or Contact</p>

    <div class="abs back-url">WWW.BRIGHTFERNYARDWORKSTEXAN.COM</div>
    <div class="abs back-phone">
      <svg width="22" height="22" viewBox="0 0 24 24" aria-hidden="true"><circle cx="12" cy="12" r="10.5" fill="none" stroke="#ffffff" stroke-width="1.5"/><path d="M9 6.5 L11 9.5 L9.8 11 Q11 13.6 13 14.4 L14.5 13.2 L17.5 15.2 L16.2 17.5 Q10 17 7 9 Z" fill="#ffffff"/></svg>
      <span>(713) 580-2143</span>
    </div>

    <div class="abs indicia">PRSRT STD<br>ECRWSS<br>U.S. POSTAGE<br>PAID<br>EDDM RETAIL</div>
    <div class="abs ecrwss">*********ECRWSS******</div>
    <div class="abs postal">Local<br>Postal Customer</div>

    <div class="abs back-brand">
      <span class="brand-dot"></span>
      <span class="brand-name">Bright Fern<br>Yard Works</span>
    </div>
    <p class="abs tagline">THE NEIGHBORHOOD'S<br>HEALTHIEST LAWN</p>
  </section>

</main>
</body>
</html>
```